Harold Penwick Sausage Label Design

Talmore Fields Corporation is seeking to create a new brand of fresh 100% Canadian pork sausage. This label will be a paper band that slips on and off foam trays. The front facing side will be 5 inches wide by 3.5 inches high. The following is some information about our brand.
Target market:
1. Working Moms
2. Stay at home moms
3. Barbeque enthusiast
Brand personality
1. Old school values – We are a family run company who believes in an honest days work
2. Modern day sensibility – We believe in being nimble and open to new ideas
3. Energetic and optimistic – We are passionate about our business and product
4. Relaxed sense of humor – We believe that it is possible to work hard and have fun
Positioning Statements:
Our sausage is the easy choice for adding flavour to your real- life family meals, that’s because:
1. It is 100% fresh Canadian product with no fillers or preservatives
2. It is a great tasting recipe with simple, natural ingredients
3. It is brought to you with good humor and integrity by a multi- generational family owned business
We are looking for a creative designer to make our ideas come to life. There are three types of designs we would like to see:
1. Rustic – a rustic, barbequing, old farm, country feel – without feeling too old
2. Modern & Simple – Very simple clean face with clean text
3. Family friendly – a label that would appeal to the everyday family with photos of the finished product
This brand does not have a name yet, please use the name “Harold Penwick “as a place holder. Please keep in mind the information provided about our brand when developing the label. Attached are pictures of some ideas we like. Please do not copy these ideas too closely, we are looking to differentiate ourselves in the market. Samples are to provide some guidance of our preferences.
Target Market(s)
1. Working Moms
2. Stay at home moms
3. Barbeque enthusiast
Colors
Designer to choose colors to be used in the design.
Look and feel
Each slider illustrates characteristics of the customer's brand and the style your logo design should communicate.

```html
<!DOCTYPE html>
<html lang="en">
<head>
<meta charset="utf-8">
<title>Harold Penwick – Mutton &amp; Mint Pork Sausages Label</title>
<link rel="stylesheet" href="https://fonts.googleapis.com/css2?family=Alfa+Slab+One&family=Yellowtail&display=block">
<style>
  :root {
    --label-green: #bccb3e;
    --cream: #fffbe8;
    --forest: #0f4a12;
    --rule: 4px;
  }
  html, body {
    margin: 0;
    padding: 0;
    overflow: hidden;
    background: var(--label-green);
  }
  .label {
    position: relative;
    width: 1200px;
    height: 840px;
    background: var(--label-green);
    overflow: hidden;
    font-family: "Alfa Slab One", Georgia, serif;
    color: var(--cream);
  }
  .rule { position: absolute; background: var(--cream); }
  .rule--h { height: var(--rule); }
  .rule--v { width: var(--rule); }

  .company {
    position: absolute;
    left: 51px; top: 70px;
    margin: 0;
    font-size: 21px;
    line-height: 24px;
    font-weight: 400;
    white-space: nowrap;
  }
  .brand-name {
    position: absolute;
    left: 38px; top: 172px;
    width: 440px; height: 240px;
  }
  .brand-name text {
    font-family: "Alfa Slab One", Georgia, serif;
    font-size: 124px;
  }
  .brand-name .shadow { fill: var(--forest); }
  .brand-name .face { fill: var(--cream); }

  .cuts-chart {
    position: absolute;
    left: 560px; top: 100px;
    width: 568px; height: 296px;
    border-radius: 140px 120px 110px 150px;
    background: radial-gradient(ellipse at 50% 50%, var(--cream) 0%, #f1f0d4 70%, #dfe2b0 100%);
    box-shadow: 0 0 0 5px var(--forest);
  }
  .country-map {
    position: absolute;
    left: 64px; top: 502px;
    width: 176px; height: 164px;
    border-radius: 30px 60px 30px 50px;
    background: var(--cream);
  }
  .script {
    position: absolute;
    margin: 0;
    font-family: "Yellowtail", "Brush Script MT", "Segoe Script", cursive;
    font-weight: 400;
    color: var(--cream);
    white-space: nowrap;
  }
  .origin {
    left: 250px; top: 474px;
    width: 140px;
    font-size: 34px;
    line-height: 30px;
    text-align: center;
  }
  .natural {
    left: 428px; top: 472px;
    font-size: 46px;
    line-height: 50px;
  }
  .flavour {
    position: absolute;
    left: 430px; top: 556px;
    margin: 0;
    font-weight: 400;
    font-size: 54px;
    line-height: 60px;
    color: var(--forest);
    white-space: nowrap;
  }
  .product-type {
    position: absolute;
    left: 438px; top: 624px;
    margin: 0;
    font-size: 31px;
    line-height: 36px;
    white-space: nowrap;
  }
  .count {
    position: absolute;
    left: 72px; top: 718px;
    font-size: 28px;
    line-height: 32px;
  }
  .weight {
    position: absolute;
    left: 194px; top: 708px;
    font-size: 31px;
    line-height: 36px;
    white-space: nowrap;
  }
  .weight .estimated { font-family: Georgia, serif; font-size: 40px; margin-left: 8px; }
  .storage {
    position: absolute;
    left: 194px; top: 750px;
    font-size: 16px;
    line-height: 20px;
    white-space: nowrap;
  }
  .description {
    position: absolute;
    left: 438px; top: 704px;
    margin: 0;
    font-size: 31px;
    line-height: 40px;
    white-space: nowrap;
  }
</style>
</head>
<body>
<main class="label">
  <p class="company">TALMORE FIELDS CORPORATION</p>
  <div class="rule rule--h" style="left:46px; top:122px; width:462px;"></div>
  <div class="rule rule--v" style="left:506px; top:46px; height:406px;"></div>

  <svg class="brand-name" viewBox="0 0 440 240" aria-label="Harold Penwick">
    <text class="shadow" x="8" y="112" textLength="420" lengthAdjust="spacingAndGlyphs">HAROLD</text>
    <text class="face" x="2" y="106" textLength="420" lengthAdjust="spacingAndGlyphs">HAROLD</text>
    <text class="shadow" x="8" y="222" textLength="420" lengthAdjust="spacingAndGlyphs">PENWICK</text>
    <text class="face" x="2" y="216" textLength="420" lengthAdjust="spacingAndGlyphs">PENWICK</text>
  </svg>

  <div class="cuts-chart" role="img" aria-label="Illustrated pig showing butcher cuts: ham, loin, shoulder, spare ribs, picnic ham, bacon"></div>

  <div class="rule rule--h" style="left:44px; top:452px; width:1108px;"></div>
  <div class="rule rule--v" style="left:406px; top:456px; height:336px;"></div>

  <div class="country-map" role="img" aria-label="Map of Canada"></div>
  <p class="script origin">100%<br>Canadian</p>

  <p class="script natural">All Natural</p>
  <div class="rule rule--h" style="left:410px; top:539px; width:742px;"></div>

  <h1 class="flavour">MUTTON &amp; MINT</h1>
  <p class="product-type">PORK SAUSAGES</p>

  <div class="rule rule--h" style="left:44px; top:685px; width:1108px;"></div>
  <div class="rule rule--v" style="left:162px; top:689px; height:103px;"></div>

  <span class="count">X6</span>
  <span class="weight">400G<span class="estimated">℮</span></span>
  <span class="storage">KEEP REFRIGERATED</span>

  <p class="description">6 MATURE MUTTON SAUSAGE,<br>INFUSED WITH MINT.</p>
</main>
</body>
</html>
```